K & D A/C Compressors' Business Card

Hello,

I need someone to create a new business card for my business. The name of my Business is: K & D A/C Compressors. I sell automotive air conditioning parts (a/c parts). I would like the business card to incorporate my logo, and to have an automotive feel to it. It is important that the business card feel like it is coming from an automotive parts business.

I already have a logo, which I will provide.

Thanks.
Updates

Project Deadline Extended Reason: I feel like extending the deadline until October 9, 2017, will allow for more time to design the business card. Thank you for your understanding. Added Monday, October 2, 2017

Target Market(s)

Consumers who need automotive a/c parts, and auto mechanics.

Industry/Entity Type

Automotive

Contact Information for Business Card

Business name: K & D A/C Compressors
Business Address: 48207 Southwest 36th Street, North Miami Beach, Florida 33162
Telephone: 305-472-1390
Fax: To be provided once I choose your design.
Website: www.kdcoolunits.example
Email: support@kdcoolunits.example
Names: To be provided once I choose your design.

Font styles to use
Sans Serif

Colors

Designer to choose colors to be used in the design.

Requirements
Must have
• The business card must include all of the "Business Card Details" and the logo I have uploaded.

```html
<!DOCTYPE html>
<html lang="en">
<head>
<meta charset="utf-8">
<title>K &amp; D A/C Compressors — Business Card</title>
<link rel="stylesheet" href="https://fonts.googleapis.com/css2?family=Montserrat:wght@400&family=Roboto:wght@300;400&display=swap">
<style>
  :root {
    --backdrop: #bccbca;
    --ink: #0c0e10;
    --paper: #ffffff;
    --cyan: #00ffff;
    --grey: #8f8f8f;
    --text-dark: #1d1d1f;
    --text-light: #ffffff;
  }
  * { margin: 0; padding: 0; box-sizing: border-box; }
  html, body { width: 1200px; height: 1200px; overflow: hidden; }
  body { background: var(--backdrop); position: relative; font-family: "Roboto", sans-serif; }

  .card {
    position: absolute; left: 158px; width: 868px; height: 508px;
    box-shadow: 0 2px 3px rgba(0,0,0,0.35);
    overflow: hidden;
  }
  .card--front { top: 46px; background: var(--ink); }
  .card--back { top: 602px; background: var(--paper); }

  .brand {
    position: absolute; left: 0; right: 0;
    display: flex; align-items: center; justify-content: center; gap: 22px;
    font-family: "Montserrat", sans-serif; font-weight: 400; color: var(--grey);
  }
  .brand__mark { width: 44px; height: 44px; background: var(--cyan); flex: none; }
  .brand__name { line-height: 1; }
  .brand__short { display: block; font-size: 72px; letter-spacing: 4px; }
  .brand__long { display: block; font-size: 38px; margin-top: 10px; }
  .card--front .brand { top: 186px; }
  .card--back .brand { top: 68px; }
  .card--back .brand__short { font-size: 62px; }
  .card--back .brand__long { font-size: 33px; }

  .band { position: absolute; top: 228px; height: 191px; }
  .band--name {
    left: 0; width: 434px; background: var(--cyan);
    color: var(--text-light); text-align: center;
    display: flex; flex-direction: column; justify-content: center;
  }
  .band--name::before {
    content: ""; position: absolute; top: 0; left: 208px;
    border-left: 13px solid transparent; border-right: 13px solid transparent;
    border-top: 13px solid var(--paper);
  }
  .band--name::after {
    content: ""; position: absolute; right: -13px; top: 82px;
    border-top: 13px solid transparent; border-bottom: 13px solid transparent;
    border-left: 13px solid var(--cyan); z-index: 2;
  }
  .band__short { font-size: 46px; font-weight: 400; letter-spacing: 2px; line-height: 1.1; }
  .band__long { font-size: 32px; font-weight: 300; line-height: 1.2; }

  .band--contact { left: 434px; right: 0; background: var(--ink); }
  .contact-list { list-style: none; position: absolute; left: 52px; top: 30px; }
  .contact-list li {
    display: flex; align-items: center; gap: 12px; height: 34.5px;
    color: var(--text-light); font-size: 21px; font-weight: 300;
  }
  .contact-list svg { width: 22px; height: 22px; fill: none; stroke: var(--cyan); stroke-width: 2; flex: none; }

  .address {
    position: absolute; left: 0; right: 0; top: 447px; text-align: center;
    color: var(--text-dark); font-size: 25px; font-weight: 400;
  }
</style>
</head>
<body>

<section class="card card--front">
  <div class="brand">
    <span class="brand__mark"></span>
    <span class="brand__name">
      <span class="brand__short">K &amp; D</span>
      <span class="brand__long">A/C Compressors</span>
    </span>
  </div>
</section>

<section class="card card--back">
  <div class="brand">
    <span class="brand__mark"></span>
    <span class="brand__name">
      <span class="brand__short">K &amp; D</span>
      <span class="brand__long">A/C Compressors</span>
    </span>
  </div>

  <div class="band band--name">
    <span class="band__short">K &amp; D</span>
    <span class="band__long">A/C Compressors</span>
  </div>

  <div class="band band--contact">
    <ul class="contact-list">
      <li>
        <svg viewBox="0 0 24 24"><path d="M3 9c2-4 16-4 18 0l-3 2-2-2H8l-2 2z" fill="#00ffff"/><rect x="6" y="12" width="12" height="8" rx="2" fill="#00ffff"/></svg>
        305-472-1390
      </li>
      <li>
        <svg viewBox="0 0 24 24"><rect x="3" y="9" width="4" height="12" fill="#00ffff"/><rect x="8" y="4" width="13" height="17" fill="#00ffff" stroke="none"/><path d="M11 10h7M11 13h7M11 16h7" stroke="#0c0e10"/></svg>
        000-111-2222
      </li>
      <li>
        <svg viewBox="0 0 24 24"><rect x="3" y="7" width="18" height="13" fill="#00ffff" stroke="none"/><path d="M3 7l9 7 9-7" stroke="#0c0e10"/></svg>
        support@kdcoolunits.example
      </li>
      <li>
        <svg viewBox="0 0 24 24"><circle cx="12" cy="12" r="9"/><ellipse cx="12" cy="12" rx="4" ry="9"/><path d="M3 12h18"/></svg>
        www.kdcoolunits.example
      </li>
    </ul>
  </div>

  <p class="address">48207 Southwest 36th Street, North Miami Beach, Florida 33162</p>
</section>

</body>
</html>
```